Newsletter Design Project

We need a template design for Mailchimp (html) newsletter (two types, one with only one property and one with several). One will be a b2b newsletter the other one a b2c.

It needs to work as a template in mailchimp and be branded like our website www.tide-vista-benalora.com

Reason: have not yet found the design that will be the one.

Target Market(s)

b2b: real estate agencies, b2c: real estate buyers in Spain in the middle and luxury segment: €350 k plus

Industry/Entity Type

Property

Requirements
Must have
• mailchimp compatible

```html
<!DOCTYPE html>
<html lang="en">
<head>
<meta charset="utf-8">
<title>Tide Vista Benalora – Property Newsletter</title>
<link rel="stylesheet" href="https://fonts.googleapis.com/css2?family=Arimo:wght@400;700&family=Didact+Gothic&display=swap">
<style>
  :root {
    --page-bg: #e6e6e6;
    --paper: #ffffff;
    --header-top: #e4e4e4;
    --band-gold: #d4c77e;
    --ink: #333333;
    --ink-soft: #444444;
    --rule: #333333;
    --bar-dark: #444444;
    --button-dark: #3a3a3a;
    --button-text: #d9cd88;
    --tweet-blue: #2ac3f3;
    --like-blue: #6f8cc6;
    --forward-green: #3b9a12;
    --photo-tone-a: #8aaac4;
    --photo-tone-b: #6f97b8;
  }
  * { box-sizing: border-box; margin: 0; padding: 0; }
  html, body {
    width: 1200px; height: 1093px; overflow: hidden;
    background: var(--page-bg);
    font-family: "Arimo", Arial, sans-serif;
    color: var(--ink);
  }
  .newsletter {
    position: absolute; left: 122px; top: 13px; width: 944px;
    background: var(--paper);
    box-shadow: 4px 4px 5px rgba(0,0,0,0.35);
  }
  .masthead {
    position: relative; height: 152px;
    background: linear-gradient(to bottom, var(--header-top), #ffffff 70%);
  }
  .brand {
    position: absolute; left: 28px; top: 26px;
    display: flex; align-items: center; gap: 12px;
  }
  .brand-mark { width: 22px; height: 22px; background: var(--ink-soft); }
  .brand-name {
    font-weight: 700; font-size: 30px; letter-spacing: 1px;
    color: var(--ink-soft); line-height: 1;
  }
  .masthead-tagline {
    position: absolute; right: 45px; top: 78px;
    font-family: "Didact Gothic", Arial, sans-serif;
    font-size: 23px; line-height: 30px; text-align: right; color: var(--ink-soft);
  }
  .feature-band {
    position: relative; height: 455px; background: var(--band-gold);
  }
  .feature-title {
    position: absolute; left: 30px; top: 44px;
    font-size: 28px; font-weight: 700; color: var(--ink-soft);
  }
  .view-button {
    position: absolute; left: 712px; top: 45px; width: 188px; height: 36px;
    border-radius: 4px; background: var(--button-dark);
    box-shadow: 2px 2px 2px rgba(0,0,0,0.3);
    color: var(--button-text); font-size: 16px; font-weight: 700;
    display: flex; align-items: center; justify-content: center;
    text-decoration: none;
  }
  .property-photo {
    position: absolute; left: 27px; top: 93px; width: 501px; height: 331px;
    border: 1px solid #333;
    background: linear-gradient(to bottom, var(--photo-tone-a), var(--photo-tone-b));
  }
  .feature-copy {
    position: absolute; left: 545px; top: 104px; width: 356px;
    font-size: 18.5px; line-height: 28px;
  }
  .feature-copy .lead { font-weight: 700; color: var(--ink); margin-bottom: 6px; }
  .feature-copy p + p { color: var(--ink-soft); font-size: 18px; }
  .details {
    position: relative; height: 311px; display: flex;
    padding: 18px 0 0 27px; gap: 40px;
  }
  .details-text { width: 501px; }
  .section-heading {
    font-size: 18px; font-weight: 700; padding-bottom: 8px;
    border-bottom: 1px solid var(--rule); margin-bottom: 10px;
  }
  .details-text p { font-size: 18px; line-height: 28px; margin-bottom: 14px; }
  .fact-sheet { width: 354px; font-size: 17px; font-weight: 700; }
  .fact-sheet .section-heading { text-align: center; }
  .fact-grid {
    display: grid; grid-template-columns: 191px 1fr; row-gap: 13px;
    line-height: 28px;
  }
  .price { text-align: right; padding-right: 34px; margin-top: 9px; }
  .share-bar {
    height: 44px; background: var(--bar-dark);
    display: flex; justify-content: flex-end; align-items: center;
    gap: 8px; padding-right: 8px;
  }
  .share-button {
    height: 31px; display: flex; align-items: center; gap: 8px;
    padding: 0 10px; color: #fff; font-size: 17px; font-weight: 700;
    text-decoration: none;
  }
  .share-button .icon { width: 12px; height: 12px; background: #fff; }
  .share-tweet { background: var(--tweet-blue); width: 102px; }
  .share-like { background: var(--like-blue); width: 75px; }
  .share-forward { background: var(--forward-green); width: 135px; }
  .site-footer {
    position: absolute; left: 122px; top: 998px; width: 954px; text-align: center;
  }
  .footer-nav { font-size: 17px; font-weight: 700; color: var(--ink); }
  .footer-nav a { color: inherit; text-decoration: none; }
  .footer-nav .sep { margin: 0 18px; }
  .copyright { margin-top: 22px; font-size: 16px; color: var(--ink); }
</style>
</head>
<body>
  <main class="newsletter">
    <header class="masthead">
      <div class="brand">
        <span class="brand-mark"></span>
        <span class="brand-name">TIDE VISTA BENALORA</span>
      </div>
      <div class="masthead-tagline">Villa Benalora - Property in Costa Alta,<br>Los Pinos, Miravela</div>
    </header>

    <section class="feature-band">
      <h1 class="feature-title">Ample villa in carib playa</h1>
      <a class="view-button" href="#">&lt;&lt; View on website</a>
      <div class="property-photo" role="img" aria-label="Property photo: villa with garden and private swimming pool"></div>
      <div class="feature-copy">
        <p class="lead">Lorem Ipsum is simply dummy text of the printing and typesetting industry. Lorem Ipsum has been the industry's standard dummy text ever since the 1500s, when an unknown printer took a galley of type and scrambled it to make a type specimen book.</p>
        <p>It has survived not only five centuries, but also the leap into electronic typesetting, remaining essentially unchanged.</p>
      </div>
    </section>

    <section class="details">
      <div class="details-text">
        <h2 class="section-heading">Description</h2>
        <p>Villa, Beachside, Furnished: Negotiable, Fitted Kitchen, Parking: Driveway, Pool Private, Garden: Private, Facing: East.</p>
        <h2 class="section-heading">Features</h2>
        <p>Air Conditioning Hot/Cold, Close to all Amenities, Covered Terrace, Detached Villa, Double Glazing, Fitted Kitchen</p>
      </div>
      <div class="fact-sheet">
        <h2 class="section-heading">REF HE263</h2>
        <div class="fact-grid">
          <span>Type: Villa</span><span>Built size: 273</span>
          <span>Beds: 3</span><span>Plot size: 631</span>
          <span>Baths: 3</span><span></span>
        </div>
        <div class="price">Price 565,000 €</div>
      </div>
    </section>

    <nav class="share-bar">
      <a class="share-button share-tweet" href="#"><span class="icon"></span>TWEET</a>
      <a class="share-button share-like" href="#"><span class="icon"></span>LIKE</a>
      <a class="share-button share-forward" href="#"><span class="icon"></span>FORWARD</a>
    </nav>
  </main>

  <footer class="site-footer">
    <div class="footer-nav">
      <a href="#">For Sale</a><span class="sep">|</span><a href="#">For Rent</a><span class="sep">|</span><a href="#">Areas</a><span class="sep">|</span><a href="#">General Info</a><span class="sep">|</span><a href="#">About us</a><span class="sep">|</span><a href="#">Contact</a>
    </div>
    <p class="copyright">Copyright 2010 Tide Vista Benalora</p>
  </footer>
</body>
</html>
```